Soy Candle Labels

We sell soy candles in recycled wine bottles. The wine bottle is cut in half and filled with pure and natural soy wax and scented with essential oils.
Our product represents good use of up cycling materials for a better use. The product is all natural and eco friendly.
You can see good use of labels and branding for a company in America that does the same thing http://larkwick-tapers.example/
Trya dn keep the label uncomplicated like the above labels.
We will need an area to hand stamp the scent. Similar to the labels used on the above website.
We would prefer to use a white or off white paper label with gold or bronze printing - limit the use of colour and keep the label simple and sophisticated.
Fernlow Candle Co. is our company name. Fernlow being the predominant name and candle co. written small underneath right justified.
Die cut labels might look better than a rectangle.
Dimensions should be 90mm Wide x 90mm High
The final design should communicate a professional and quality product. But stay modern and professional. Clean, elegant and sophisticated.
Can use wording such as: Hand Poured, Premium Soy Wax, All Natural, Up cycled
Have a look at the attached image for the look and feel we are going for.
Updates
Designers are having a little bit of trouble interpreting the brief into a viable design. To assist perhaps you can look at WINE LABELS on google images. Design your label around an existing style wine label to give the canld ethe feel of being a bottle of wine. Get creative! :)
Reason: We require more designs. We havnt quite got what were looking for.
Please see brief.
Industry/Entity Type
Printing
Look and feel
Each slider illustrates characteristics of the customer's brand and the style your logo design should communicate.

```html
<!DOCTYPE html>
<html lang="en">
<head>
<meta charset="utf-8">
<title>Fernlow Candle Co. — Soy Candle Label</title>
<link rel="stylesheet" href="https://fonts.googleapis.com/css2?family=Barlow:wght@400;500&family=Open+Sans:wght@400&family=Pathway+Gothic+One&display=swap">
<style>
  :root {
    --backdrop: #3a1d10;
    --paper: #fdfcf6;
    --ink: #3a1d10;
    --rule: #4a2a1c;
  }
  html, body {
    margin: 0;
    padding: 0;
    width: 1200px;
    height: 1000px;
    overflow: hidden;
    background: var(--backdrop);
  }
  .canvas {
    position: relative;
    width: 1200px;
    height: 1000px;
    background: var(--backdrop);
  }
  .label {
    position: absolute;
    left: 132px;
    top: 30px;
    width: 942px;
    height: 942px;
    background: var(--paper);
    border-radius: 24px;
  }
  .label-frame {
    position: absolute;
    left: 16px;
    top: 16px;
    width: 908px;
    height: 908px;
    border: 1.5px solid var(--rule);
    border-radius: 18px;
    box-sizing: border-box;
  }
  .claims {
    position: absolute;
    left: 46px;
    top: 42px;
    color: var(--ink);
    font-family: "Barlow", sans-serif;
    font-weight: 500;
  }
  .claims-title {
    margin: 0;
    font-size: 42px;
    line-height: 52px;
    letter-spacing: 0.5px;
  }
  .claims-line {
    margin: 0;
    font-size: 30px;
    line-height: 40px;
  }
  .claims-line.small {
    font-size: 27px;
    line-height: 36px;
  }
  .scent-stamp {
    position: absolute;
    left: 633px;
    top: 47px;
    width: 230px;
    height: 230px;
  }
  .scent-word {
    position: absolute;
    left: 674px;
    top: 76px;
    width: 26px;
    color: var(--ink);
    font-family: "Barlow", sans-serif;
    font-weight: 500;
    font-size: 26px;
    line-height: 29px;
    text-align: center;
  }
  .brand {
    position: absolute;
    right: 78px;
    top: 400px;
    text-align: right;
    color: var(--ink);
  }
  .brand-name {
    margin: 0;
    font-family: "Barlow", sans-serif;
    font-weight: 400;
    font-size: 150px;
    line-height: 170px;
    letter-spacing: 2px;
  }
  .brand-sub {
    margin: 4px 0 0;
    font-family: "Open Sans", sans-serif;
    font-size: 31px;
    line-height: 36px;
  }
  .footer-note {
    position: absolute;
    bottom: 62px;
    margin: 0;
    color: var(--ink);
    font-family: "Pathway Gothic One", sans-serif;
    font-size: 48px;
    line-height: 52px;
  }
  .footer-note.origin { left: 46px; }
  .footer-note.material { right: 46px; }
</style>
</head>
<body>
<main class="canvas">
  <section class="label">
    <div class="label-frame"></div>

    <div class="claims">
      <p class="claims-title">Hand Poured</p>
      <p class="claims-line">All Natural Soy</p>
      <p class="claims-line small">320 gm of Premium Soy Wax</p>
    </div>

    <svg class="scent-stamp" viewBox="0 0 230 230" aria-hidden="true">
      <circle cx="115" cy="115" r="114" fill="none" stroke="var(--rule)" stroke-width="1"/>
    </svg>
    <div class="scent-word">S<br>C<br>E<br>N<br>T</div>

    <div class="brand">
      <p class="brand-name">Fernlow</p>
      <p class="brand-sub">Candle Co.</p>
    </div>

    <p class="footer-note origin">Product of Australia</p>
    <p class="footer-note material">Up-Cycled wine bottle</p>
  </section>
</main>
</body>
</html>
```